4Star Hotel looking for web design

Hello everyone,
We are located in Cambodia, the hotel should open in 2-3 months. The name will be Velmora-Boutique Hotel. We are looking for a webdesign which is professional, elegant and SIMPLE.
All informations should be easy to find. We are quite open to proposition but we would like to the home page:
-a carousel with around 5-8 picture
-Little menu where we can book a room
By the way, we would like a page for our restaurant, gallery, contact page for description of the rooms. I add some old pictures.
I give an example of what we are expecting:
www.quenrostays.com/tovelspring
We hope that we are proposing a good job for you guys. Have fun and Thanks.
Oh and the winner ( or someone he had choose) of course have free night in our presidential suite
Target Market(s)
We are looking for european Market. Let s say people middle age who are willing to travel in difficult area
Industry/Entity Type
Hotel
Coding
Coded - Design and coding required
Number of Pages Required
5+ page
Requirements
Must have
- Simple, simple and Simple
- Carousel
- place for book a room
- during booking, a menu for select room , and after that another menu for propose like tour in town, taxi, flower, bottle of champagne for example
- during all the process, the customer should be able to know at what step it is and can stop and come back after
- Have to be perfect for smartphone
- Price with drawbar for they know how much they earn with our reduction
Nice to have
- during the process of information (name, adress, tel...), it would be great if they can fill it with a button facebook, google plus, lindkdin, instagram ....
- then a button share on facebook, twitter for know that they book in our hotel
- At the end of the booking, a flashcode with the recapitulatif that customer can scan.

```html
<!DOCTYPE html>
<html lang="en">
<head>
<meta charset="utf-8">
<title>Velmora Boutique Hotel</title>
<link href="https://fonts.googleapis.com/css2?family=Open+Sans:wght@300;400;600;700&display=swap" rel="stylesheet">
<style>
:root{
  --orange:#ec8a1c;
  --orange-dark:#d9770e;
  --brown:#6e2a17;
  --brown-deep:#3b1c12;
  --brown-footer:#2f1710;
  --topbar:#2b2b2b;
  --ink:#333;
  --muted:#777;
  --light:#ececec;
  --white:#fff;
  --red:#d8232a;
}
*{box-sizing:border-box;margin:0;padding:0}
html,body{width:1200px;height:2624px;overflow:hidden}
body{font-family:"Open Sans",Arial,sans-serif;color:var(--ink);background:var(--white)}
a{color:inherit;text-decoration:none}

.topbar{height:40px;background:var(--topbar);color:#ddd;font-size:14px;display:flex;align-items:center;justify-content:space-between;padding:0 60px}
.topbar .phone{display:flex;align-items:center;gap:8px}
.social{display:flex;gap:8px}
.social span{width:22px;height:22px;border-radius:50%;background:#555;display:block}

.header{height:92px;display:flex;align-items:center;justify-content:space-between;padding:0 60px}
.brand{display:flex;align-items:center;gap:10px;background:var(--brown);color:var(--white);padding:12px 18px;font-weight:600;font-size:18px}
.brand i{width:14px;height:14px;background:var(--orange);display:block}
.nav-wrap{text-align:right}
.util{font-size:12px;color:var(--muted);margin-bottom:10px}
.util b{color:var(--ink)}
.nav{display:flex;gap:0;font-size:13px;font-weight:600;text-transform:uppercase}
.nav a{padding:0 12px;border-left:1px solid #ccc}
.nav a:first-child{border:0;color:var(--orange)}

.hero{height:556px;position:relative;background:linear-gradient(135deg,#7a4a24 0%,#c99a5c 45%,#e8c996 60%,#8a5a30 100%)}
.hero-copy{position:absolute;left:110px;top:200px;color:var(--white)}
.hero-copy h1{font-size:50px;font-weight:600;letter-spacing:1px;background:rgba(0,0,0,.35);display:inline-block;padding:2px 12px}
.hero-copy p{font-size:38px;font-weight:300;background:rgba(0,0,0,.35);display:inline-block;padding:0 12px;margin-top:6px}
.btn{display:inline-block;background:var(--orange);color:var(--white);font-weight:700;font-size:13px;padding:10px 18px;text-transform:uppercase}
.hero-copy .btn{margin-top:18px;background:var(--red)}

.booking{height:92px;background:var(--orange);display:flex;align-items:center;padding:0 60px;gap:18px}
.field{color:var(--white);font-size:12px}
.field div{width:110px;height:28px;background:var(--white);margin-top:5px}
.field.wide div{width:150px}
.book-cta{margin-left:auto;display:flex;align-items:center;gap:12px}
.book-cta .dot{width:56px;height:56px;border-radius:50%;border:3px solid var(--white);display:flex;align-items:center;justify-content:center}
.book-cta .btn{background:var(--brown-deep)}

.about{height:288px;background:var(--light);text-align:center;padding-top:30px}
h2{font-size:34px;font-weight:400;color:var(--ink)}
.lead{width:900px;margin:10px auto 0;font-size:12px;color:var(--muted);line-height:1.6}
.features{display:flex;justify-content:center;gap:110px;margin-top:34px}
.feature{display:flex;align-items:center;gap:16px;font-size:18px;font-weight:600;text-transform:uppercase;text-align:left;line-height:1.2}
.feature .ico{width:72px;height:72px;border-radius:50%;background:var(--brown);display:flex;align-items:center;justify-content:center}

.gallery{height:580px;text-align:center;padding-top:30px}
.grid{display:grid;grid-template-columns:repeat(4,210px);gap:12px;justify-content:center;margin-top:40px}
.ph{height:152px}

.offers{height:440px;background:linear-gradient(180deg,#1d1d24 0%,#3a3640 60%,#6b4b3c 100%);color:var(--white);text-align:center;padding-top:34px}
.offers h2{color:var(--white);font-size:30px}
.offers .sub{font-size:24px;font-weight:300;margin-top:4px}
.cards{display:flex;justify-content:center;gap:20px;margin-top:28px}
.card{width:230px;height:230px}
.card.info{background:var(--white);color:var(--ink);text-align:left;padding:18px;font-size:12px;line-height:1.8}
.card.info h3{color:var(--red);font-size:14px;font-weight:700}
.card.info s{color:var(--muted)}
.card.info .btn{display:block;text-align:center;margin-top:14px;background:var(--brown-deep)}

.quote{height:180px;display:flex;align-items:center;justify-content:center;gap:28px}
.quote .clock{width:90px;height:90px;border-radius:50%;background:var(--brown-deep);color:var(--white);display:flex;align-items:center;justify-content:center;font-weight:700;font-size:24px}
.quote .txt{width:560px}
.quote h4{font-size:22px;font-weight:600}
.quote p{font-size:12px;color:var(--muted);line-height:1.6;margin-top:4px}
.quote .btn{border:2px solid var(--orange);background:transparent;color:var(--orange);padding:14px 22px}

.footer{height:336px;background:var(--brown-footer);color:#c9b4aa;padding:40px 100px 0;display:flex;gap:70px;font-size:13px}
.footer h5{color:var(--orange);font-size:16px;font-weight:600;text-transform:uppercase;margin-bottom:12px}
.footer li{list-style:none;line-height:1.9}
.footer .col-logo{margin-left:auto;text-align:center}
.footer .brand{margin-bottom:18px}
.copy{height:60px;background:#241009;color:#9a847a;font-size:12px;display:flex;align-items:center;justify-content:center}
</style>
</head>
<body>

<div class="topbar">
  <span class="phone">
    <svg width="14" height="14" viewBox="0 0 24 24" fill="#ddd"><path d="M6.6 10.8a15 15 0 006.6 6.6l2.2-2.2a1 1 0 011-.25 11.4 11.4 0 003.6.57 1 1 0 011 1V20a1 1 0 01-1 1A17 17 0 013 4a1 1 0 011-1h3.5a1 1 0 011 1c0 1.25.2 2.45.57 3.57a1 1 0 01-.25 1z"/></svg>
    123-456-7890
  </span>
  <div class="social"><span></span><span></span><span></span><span></span><span></span></div>
</div>

<header class="header">
  <a class="brand" href="#"><i></i>Velmora Boutique Hotel</a>
  <div class="nav-wrap">
    <div class="util">Contact Us &nbsp;|&nbsp; Careers &nbsp;|&nbsp; <b>CALL US NOW: 123-456-7890</b></div>
    <nav class="nav">
      <a href="#">Home</a><a href="#">Accommodation</a><a href="#">Restaurant &amp; Bar</a><a href="#">Meeting &amp; Events</a><a href="#">Blog</a><a href="#">Special Packages</a>
    </nav>
  </div>
</header>

<section class="hero" role="img" aria-label="Warm-lit hotel bedroom with twin beds, lamps and a television">
  <div class="hero-copy">
    <h1>VELMORA</h1><br>
    <p>I feel comfortable here</p><br>
    <a class="btn" href="#">Read more</a>
  </div>
</section>

<form class="booking">
  <div class="field">Check in<div></div></div>
  <div class="field">Check out<div></div></div>
  <div class="field">Rooms<div></div></div>
  <div class="field">Guests<div></div></div>
  <div class="field wide">Promotion Code<div></div></div>
  <div class="book-cta">
    <span class="dot"><svg width="26" height="26" viewBox="0 0 24 24" fill="none" stroke="#fff" stroke-width="2"><rect x="3" y="5" width="18" height="16"/><path d="M3 10h18M8 3v4M16 3v4"/></svg></span>
    <a class="btn" href="#">Check availability</a>
  </div>
</form>

<section class="about">
  <h2>About Us</h2>
  <p class="lead">Set in the quiet heart of the province, our boutique hotel blends local craft with modern comfort. Every room opens to calm gardens, and our team is ready to plan tours, transfers and dining so that each guest can rest, explore and feel at home from the very first day of their stay.</p>
  <div class="features">
    <div class="feature"><span class="ico"><svg width="32" height="32" viewBox="0 0 24 24" fill="none" stroke="#fff" stroke-width="2"><path d="M7 2v9M4 2v5a3 3 0 006 0V2M7 11v11M17 2c-2 2-3 5-3 8h3v12"/></svg></span>Royal<br>Resturant</div>
    <div class="feature"><span class="ico"><svg width="32" height="32" viewBox="0 0 24 24" fill="none" stroke="#fff" stroke-width="2"><path d="M4 4h16l-8 9zM12 13v8M8 21h8"/></svg></span>Lemon<br>Bar</div>
    <div class="feature"><span class="ico"><svg width="32" height="32" viewBox="0 0 24 24" fill="none" stroke="#fff" stroke-width="2"><path d="M3 20V9l9-5 9 5v11M3 20h18M9 20v-6h6v6"/></svg></span>Hotel<br>Lounge</div>
  </div>
</section>

<section class="gallery">
  <h2>Over Gallery</h2>
  <p class="lead">A look around our rooms, restaurant, lounge and pool. Browse the spaces where guests relax, dine and gather, and picture your own stay with us before you book your dates online.</p>
  <div class="grid">
    <div class="ph" role="img" aria-label="Hotel bedroom" style="background:linear-gradient(135deg,#8a6a4a,#d9c2a0)"></div>
    <div class="ph" role="img" aria-label="Restaurant interior" style="background:linear-gradient(135deg,#4a2e1e,#a27a52)"></div>
    <div class="ph" role="img" aria-label="Dining room" style="background:linear-gradient(135deg,#5a3a28,#c8a07a)"></div>
    <div class="ph" role="img" aria-label="Suite with sofa" style="background:linear-gradient(135deg,#7a5a3c,#e0cdb0)"></div>
    <div class="ph" role="img" aria-label="Lobby at night" style="background:linear-gradient(135deg,#3a2418,#a06a38)"></div>
    <div class="ph" role="img" aria-label="Bar counter" style="background:linear-gradient(135deg,#2a1c14,#8a5a34)"></div>
    <div class="ph" role="img" aria-label="Lounge seating" style="background:linear-gradient(135deg,#6a4a34,#caa884)"></div>
    <div class="ph" role="img" aria-label="Pool terrace" style="background:linear-gradient(135deg,#3c6a8a,#a8c8d8)"></div>
  </div>
</section>

<section class="offers">
  <h2>OUR OFFERS</h2>
  <p class="sub">Giving customers a clear path to achieving their objectives</p>
  <div class="cards">
    <div class="card" role="img" aria-label="Summer sale promotion artwork" style="background:linear-gradient(160deg,#3fb0d8,#f0c83a 70%,#e8502a)"></div>
    <div class="card info">
      <h3>30% OFF - October Exclusive Sales</h3>
      From: <s>$129.00</s> <b>$89.99</b><br>
      Booking Period: from 09 Oct 2015<br>
      Staying Period: 10 Oct - 31 Dec 2015<br>
      <a class="btn" href="#">Details</a>
    </div>
    <div class="card" role="img" aria-label="Red sale up to 70 percent off promotion artwork" style="background:linear-gradient(160deg,#e0262c,#b3141a)"></div>
  </div>
</section>

<section class="quote">
  <div class="clock">24h</div>
  <div class="txt">
    <h4>Have a question or need a custom quote?</h4>
    <p>Our front desk team is here around the clock. Tell us your travel plans and we will prepare a tailored offer with rooms, tours and transfers within one day.</p>
  </div>
  <a class="btn" href="#">Get started now for free</a>
</section>

<footer class="footer">
  <div>
    <h5>Quick Links</h5>
    <ul><li>Home</li><li>Accommodation</li><li>Restaurant &amp; Bar</li><li>Meeting &amp; Events</li><li>Blog</li><li>Special Packages</li></ul>
  </div>
  <div>
    <h5>Company</h5>
    <ul><li>About us</li><li>We are hiring</li><li>Meet My team</li><li>Careers</li><li>Terms of use</li><li>Privacy policy</li></ul>
  </div>
  <div>
    <h5>Contact Info</h5>
    <ul><li>NYZ St, Riverline</li><li>City, State, Country</li><li>Telephone: +1 123-456-7890</li><li>Fax: +1 123-456-7890</li><li>E-mail: stay@velmorahotel.com</li></ul>
  </div>
  <div class="col-logo">
    <div class="brand"><i></i>Velmora Boutique Hotel</div>
    <div class="social" style="justify-content:center"><span></span><span></span><span></span><span></span><span></span></div>
  </div>
</footer>
<div class="copy">© 2015 Velmora Boutique Hotel. All Rights Reserved.</div>

</body>
</html>
```